Education related business need name card design

We need name card design for long term study agent.
Company name is Harbor Lantern.
We support clients to connect to the world.
Clients are Japanese family who has primary and secondary school students.

Company Logo is reflection of the globe and HL (Harbor Lantern).
Since business is related to education, we would like to show reliability and love to see the world map (atlas) in the name card.

Target Market(s)

late 30's to 50's parents of primary and secondary students who are enthusiastic for education. Secondary school management

Industry/Entity Type

Education

Contact Information for Business Card

Company name, Address, Official position, Name, Phone number, Mobile number, email address,

Font styles to use
Serif
Other font styles liked:
• Century Gothic(logo)

Requirements
Must have
• Since businee is related to education, we would like to show reliability and love to see the world map (atlas) in the name card.

```html
<!DOCTYPE html>
<html lang="en">
<head>
<meta charset="utf-8">
<title>Harbor Lantern – Name Card</title>
<link rel="stylesheet" href="https://fonts.googleapis.com/css2?family=Questrial&family=Roboto:wght@400&family=Maven+Pro:wght@400;500;600&display=swap">
<style>
  :root {
    --backdrop: #000000;
    --card-white: #ffffff;
    --atlas-tint: #e4e7f4;
    --brand-navy: #2b3178;
    --brand-blue: #2a7cc1;
    --mark-blue: #1f7dc8;
    --text-light: #ffffff;
  }
  * { box-sizing: border-box; margin: 0; padding: 0; }
  html, body {
    width: 890px;
    height: 1200px;
    overflow: hidden;
    background: var(--backdrop);
  }
  .canvas {
    position: relative;
    width: 890px;
    height: 1200px;
  }

  /* Front face */
  .card-front {
    position: absolute;
    left: 48px;
    top: 51px;
    width: 787px;
    height: 524px;
    background: var(--card-white);
    overflow: hidden;
  }
  .atlas-area {
    position: absolute;
    left: 20px;
    top: 8px;
    width: 760px;
    height: 490px;
    background: radial-gradient(ellipse 52% 50% at 50% 45%, var(--atlas-tint) 0%, rgba(228,231,244,0.85) 55%, rgba(228,231,244,0) 100%);
  }
  .brand-dot {
    position: absolute;
    left: 300px;
    top: 82px;
    width: 184px;
    height: 184px;
    border-radius: 50%;
    background: var(--mark-blue);
  }
  .brand-name {
    position: absolute;
    left: 0;
    width: 100%;
    top: 284px;
    text-align: center;
    font-family: "Questrial", "Century Gothic", sans-serif;
    font-size: 34px;
    font-weight: 400;
    color: var(--brand-navy);
    letter-spacing: 0.3px;
  }
  .front-web {
    position: absolute;
    left: 0;
    width: 100%;
    top: 445px;
    text-align: center;
    font-family: "Roboto", sans-serif;
    font-size: 20px;
    color: var(--brand-navy);
  }

  /* Back face */
  .card-back {
    position: absolute;
    left: 48px;
    top: 605px;
    width: 787px;
    height: 525px;
    background: var(--brand-blue);
    overflow: hidden;
    font-family: "Maven Pro", sans-serif;
    color: var(--text-light);
  }
  .side-wordmark {
    position: absolute;
    left: 22px;
    top: 495px;
    transform-origin: 0 0;
    transform: rotate(-90deg);
    font-family: "Maven Pro", sans-serif;
    font-size: 52px;
    font-weight: 400;
    color: var(--brand-navy);
    white-space: nowrap;
    line-height: 1;
  }
  .contact-block {
    position: absolute;
    right: 21px;
    text-align: right;
    font-size: 21px;
    line-height: 26px;
    white-space: nowrap;
  }
  .person { top: 54px; }
  .person-name { font-weight: 600; letter-spacing: 0.3px; }
  .address { top: 210px; word-spacing: 6.5px; }
  .online { top: 391px; }
</style>
</head>
<body>
<main class="canvas">
  <section class="card-front">
    <div class="atlas-area" role="img" aria-label="Faint world map atlas spread across the card"></div>
    <div class="brand-dot"></div>
    <h1 class="brand-name">Harbor Lantern Pte.Ltd.</h1>
    <p class="front-web">www.harborlantern.com</p>
  </section>

  <section class="card-back">
    <div class="side-wordmark">harborlantern</div>
    <div class="contact-block person">
      <p class="person-name">NAMENAMENAME NAMENAME</p>
      <p>Designation</p>
      <p>Ph: +000 - 0000 000</p>
    </div>
    <div class="contact-block address">
      <p>Address line 1 Address line 1 Address line 1</p>
      <p>Address line 2 Address line 2</p>
      <p>Address line 3</p>
    </div>
    <div class="contact-block online">
      <p>info@harborlantern.com</p>
      <p>www.harborlanternpl.com</p>
    </div>
  </section>
</main>
</body>
</html>
```